Premium modern eliquids labels 84.5 x 80 mm

I am looking for modern graphics for the labels of a new eliquid line that will have 4 different types of eliquids. It will have a tobacco one (brown colours maybe), a fruity one (bright colours maybe), a minty one (green colours maybe) and a creamy one (beige colours maybe).
I will need one of them to see how the design is, that design will have to be adapted to the other 3 colours of the label.
The brand logo is attached. I also attached a sample of what is mandatory to write on the label, you can change size, place and font of what is written, the only thing that cannot be reduced is the yellow parts. I attach the bottle that we will use.The size of the label is 84.5 x 80 mm (base x height).

Target Market(s)

vapers

Requirements
Must have
• My project must have one of the labels.

```html
<!DOCTYPE html>
<html lang="it">
<head>
<meta charset="utf-8">
<title>Velvet Drop – Silky Strawberry &amp; Vanilla label</title>
<link href="https://fonts.googleapis.com/css2?family=Archivo:wght@600;800&family=Barlow:wght@400;600&display=swap" rel="stylesheet">
<style>
  :root {
    --brand-red: #ec1a45;
    --peach: #fcd29a;
    --peach-light: #fde6c4;
    --cream: #fdf6e6;
    --ink: #141414;
    --recycle-yellow: #fcc92e;
    --page: #ffffff;
  }
  * { box-sizing: border-box; margin: 0; padding: 0; }
  html, body { width: 705px; height: 1200px; overflow: hidden; background: var(--page); }

  .label {
    position: absolute; left: 20px; top: 285px;
    width: 665px; height: 629px; overflow: hidden;
    background: radial-gradient(circle at 50% 55%, var(--peach-light) 0%, var(--peach) 60%);
    font-family: "Barlow", sans-serif;
  }
  .label__band { position: absolute; left: 0; top: 0; width: 665px; height: 140px; }
  .label__foot { position: absolute; left: 0; bottom: 0; width: 100%; height: 8px; background: var(--brand-red); }

  .brand {
    position: absolute; left: 0; top: 48px; width: 100%;
    display: flex; justify-content: center; align-items: center; gap: 9px;
    color: #fff; font-family: "Archivo", sans-serif; font-weight: 800;
    font-size: 34px; letter-spacing: 1px;
  }
  .brand__dot { width: 14px; height: 14px; border-radius: 50%; background: #fff; }

  .info-box {
    position: absolute; top: 140px; width: 152px; height: 466px;
    border: 1px solid var(--brand-red); border-radius: 12px;
    color: var(--brand-red);
  }
  .info-box--left { left: 23px; }
  .info-box--right { left: 488px; }
  .info-box__title { position: absolute; left: 12px; top: 10px; font-weight: 600; font-size: 13.5px; }
  .info-box__body { position: absolute; left: 12px; top: 28px; font-size: 13.5px; line-height: 18.3px; }
  .info-box__rule { position: absolute; left: 5px; right: 5px; height: 1px; background: var(--brand-red); }
  .info-box--right .info-box__rule { left: 13px; right: 13px; }
  .info-box__legal { position: absolute; left: 0; top: 0; }

  .recycle { position: absolute; left: 24px; font-family: "Archivo", sans-serif; color: var(--ink); }
  .recycle__tag {
    background: var(--recycle-yellow); font-weight: 800; display: inline-block;
    font-size: 14px; line-height: 12.5px; padding: 3px 5px; text-align: center;
  }
  .recycle__part { font-weight: 600; font-size: 11px; display: block; margin: 4px 0 4px 2px; }
  .recycle__code { background: var(--recycle-yellow); font-weight: 800; font-size: 16px; padding: 5px 7px 4px; display: inline-block; letter-spacing: 1px; }

  .disposal { position: absolute; left: 35px; top: 390px; }
  .net { position: absolute; left: 0; width: 100%; top: 443px; text-align: center; font-weight: 600; font-size: 14px; }

  .flavour-art {
    position: absolute; left: 208px; top: 132px; width: 250px; height: 478px;
    background: radial-gradient(ellipse at 50% 30%, #f06f8a 0%, #f6c2c8 30%, var(--cream) 60%, rgba(253,246,230,0) 75%);
    border-radius: 45% 45% 40% 40%;
  }
  .flavour-name {
    position: absolute; left: 0; width: 100%; top: 298px; text-align: center;
    font-family: "Archivo", sans-serif; font-weight: 800; color: var(--brand-red);
    font-size: 56px; line-height: 1;
  }
  .flavour-sub {
    position: absolute; left: 0; width: 100%; top: 360px; text-align: center;
    font-family: "Archivo", sans-serif; font-weight: 800; font-size: 13px; color: var(--ink);
  }
</style>
</head>
<body>
<main class="label">
  <svg class="label__band" viewBox="0 0 665 140" aria-hidden="true">
    <path d="M0 0 H665 V94 C600 88 540 92 470 112 C400 134 360 142 320 138 C270 132 230 105 160 88 C100 74 50 74 0 80 Z" fill="var(--brand-red)"/>
  </svg>

  <div class="brand"><span class="brand__dot"></span>VELVET DROP</div>

  <section class="info-box info-box--left">
    <h2 class="info-box__title">INGREDIENTI:</h2>
    <p class="info-box__body">Glicole,<br>Propilenico,<br>Sostanze,<br>Aromatizzanti</p>
    <div class="info-box__rule" style="top:105px"></div>
    <svg class="info-box__legal" width="152" height="466" aria-label="Dati di produzione">
      <line x1="36" y1="113" x2="36" y2="444" stroke="var(--brand-red)" stroke-width="1"/>
      <g fill="var(--brand-red)" font-family="Barlow, sans-serif" font-size="12.5">
        <text transform="translate(23 444) rotate(-90)" font-weight="600">L.VD20 - 014-PES-D.PROD.15-03-2024 D.SC.14-03-2026</text>
        <text transform="translate(70 444) rotate(-90)" font-weight="600">PRODOTTO E CONFEZIONATO</text>
        <text transform="translate(88 444) rotate(-90)">DA Lumen Vapor srl, Via Aurora 18, 10100 Torino,</text>
        <text transform="translate(105 444) rotate(-90)">P.i.00000000000</text>
        <text transform="translate(123 444) rotate(-90)">Tel. +39 011 5550142 | info@lumenvapor.it</text>
      </g>
    </svg>
  </section>

  <div class="flavour-art" role="img" aria-label="Strawberry cake slice, vanilla ice cream scoop, meringues and vanilla flowers in a swirl of cream"></div>
  <h1 class="flavour-name">Silky</h1>
  <p class="flavour-sub">STRAWBERRY &amp; VANILLA</p>

  <section class="info-box info-box--right">
    <h2 class="info-box__title">ISTRUZIONI D’USO:</h2>
    <p class="info-box__body">Agitare bene prima<br>dell’utilizzo. Diluire<br>nelle percentuali<br>consigliate sul<br>nostro sito.<br>Conservare in luogo<br>fresco e asciutto</p>
    <div class="info-box__rule" style="top:166px"></div>

    <div class="recycle" style="top:186px">
      <span class="recycle__tag">RACCOLTA<br>PLASTICA</span>
      <span class="recycle__part">ETICHETTA</span>
      <span class="recycle__code">PAP 5</span>
    </div>
    <div class="recycle" style="top:281px">
      <span class="recycle__tag">RACCOLTA<br>PLASTICA</span>
      <span class="recycle__part" style="margin-left:6px">FLACONE</span>
      <span class="recycle__code">PET 1</span>
    </div>

    <div class="info-box__rule" style="top:381px"></div>
    <svg class="disposal" width="80" height="44" viewBox="0 0 80 44" aria-label="Raccolta differenziata">
      <g fill="none" stroke="var(--brand-red)" stroke-width="1.6" stroke-linejoin="round">
        <path d="M10 14 L16 4 L22 14"/><path d="M19 8 L22 14 L16 14"/>
        <path d="M26 20 L30 30 L20 30"/><path d="M23 26 L20 30 L23 34"/>
        <path d="M14 30 L3 30 L8 20"/><path d="M6 24 L8 20 L12 22"/>
      </g>
      <g fill="var(--brand-red)">
        <path d="M38 20 H54 L52 40 H40 Z" fill="none" stroke="var(--brand-red)" stroke-width="2.5"/>
        <circle cx="63" cy="5" r="4"/>
        <path d="M58 11 H68 V28 H66 V42 H62 V28 H60 V42 H56 V22 L50 16 L53 13 L58 18 Z"/>
      </g>
    </svg>
    <p class="net">20 ML NET</p>
  </section>

  <div class="label__foot"></div>
</main>
</body>
</html>
```